A property investment company, looking to provide lovely sustainable homes for familys and individua

For a small investment business i am starting which will buy and refurbish unloved houses and apartments to rent out or resell. the company name is my family surname (HARGREAVE). <br/>i would like the design to be simple with maybe some emphasis on an ethical and sustainable/environmentally friendly approach with a branding of maybe trees blended with some houses and or apartments.<br/>The colours i like for this design would be mainly green on either a white or black background.
Target Market(s)
This business card is to be used for professional people such as estate agents
mortgage brokers, solicitors and trades people.
Industry/Entity Type
Real Estate
Contact Information for Business Card
owner/director-Martin hargreave
e-mail-martin@hwlettings.co.uk
website-hargreavehomeholdings.co.uk
mobile-07934560218
landline-02086543107

```html
<!DOCTYPE html>
<html lang="en">
<head>
<meta charset="utf-8">
<title>Hargreave Business Card</title>
<link rel="stylesheet" href="https://fonts.googleapis.com/css2?family=Cinzel:wght@500&family=PT+Serif:wght@400;700&display=swap">
<style>
  :root {
    --page-bg: #141517;
    --card-bg: #202426;
    --silver: #b8bcc1;
    --green: #8cc63f;
    --white: #f2f2f2;
    --muted: #7d8287;
  }
  * { box-sizing: border-box; margin: 0; padding: 0; }
  html, body { width: 1200px; height: 800px; overflow: hidden; background: var(--page-bg); }
  .canvas {
    position: relative; width: 1200px; height: 800px;
    display: flex; align-items: center; justify-content: center; gap: 40px;
  }
  .card {
    position: relative; width: 540px; height: 310px;
    background: var(--card-bg); overflow: hidden;
    box-shadow: 0 18px 40px rgba(0,0,0,.55);
  }
  .card-front { display: flex; align-items: center; justify-content: center; }
  .brand-name {
    font-family: "Cinzel", serif; font-weight: 500; letter-spacing: 3px; white-space: nowrap;
  }
  .card-front .brand-name { font-size: 46px; color: var(--silver); }
  .card-back .brand-name {
    position: absolute; left: 34px; top: 150px; font-size: 30px; color: var(--green);
  }
  .divider {
    position: absolute; left: 278px; top: 48px; width: 1px; height: 150px;
    background: linear-gradient(to bottom, transparent, var(--muted), transparent);
  }
  .person { position: absolute; left: 302px; top: 50px; font-family: "PT Serif", serif; }
  .person-name {
    font-size: 19px; font-weight: 700; font-variant: small-caps; color: var(--white); letter-spacing: .5px;
  }
  .person-role { font-size: 14px; color: var(--green); margin-top: 1px; }
  .contact-list {
    position: absolute; left: 302px; top: 118px; list-style: none;
    font-family: "PT Serif", serif; font-size: 12.5px; color: var(--white);
  }
  .contact-list li { display: flex; align-items: center; gap: 9px; height: 22px; white-space: nowrap; }
  .contact-list svg { width: 12px; height: 12px; flex: none; }
  .accent { color: var(--green); }
  .address {
    position: absolute; left: 34px; bottom: 34px;
    font-family: "PT Serif", serif; font-size: 13px; color: var(--white); letter-spacing: .6px;
  }
  .stripe { position: absolute; left: 0; right: 0; bottom: 0; height: 9px; background: var(--green); }
</style>
</head>
<body>
<main class="canvas">
  <section class="card card-front">
    <span class="brand-name">HARGREAVE</span>
  </section>

  <section class="card card-back">
    <span class="brand-name">HARGREAVE</span>
    <div class="divider"></div>
    <div class="person">
      <p class="person-name">Martin Hargreave</p>
      <p class="person-role">Director</p>
    </div>
    <ul class="contact-list">
      <li>
        <svg viewBox="0 0 24 24" aria-hidden="true"><path fill="#8cc63f" d="M6.6 10.8a15 15 0 0 0 6.6 6.6l2.2-2.2a1 1 0 0 1 1-.25 11.4 11.4 0 0 0 3.6.57 1 1 0 0 1 1 1V20a1 1 0 0 1-1 1A17 17 0 0 1 3 4a1 1 0 0 1 1-1h3.5a1 1 0 0 1 1 1c0 1.250.2 2.45.57 3.57a1 1 0 0 1-.25 1z"/></svg>
        07700 900218
      </li>
      <li>
        <svg viewBox="0 0 24 24" aria-hidden="true"><path fill="#8cc63f" d="M2 5h20v14H2z"/><path fill="none" stroke="#202426" stroke-width="2" d="M2 5l10 8 10-8"/></svg>
        martin@hargreave.example
      </li>
      <li>
        <svg viewBox="0 0 24 24" aria-hidden="true"><circle cx="12" cy="12" r="10" fill="#8cc63f"/><path fill="none" stroke="#202426" stroke-width="1.5" d="M2 12h20M12 2c3 3 3 17 0 20M12 2c-3 3-3 17 0 20"/></svg>
        <span>www.<span class="accent">hargreavehomes</span>.example</span>
      </li>
    </ul>
    <p class="address">PO Box 48, Elmfield Road, Bromley</p>
    <div class="stripe"></div>
  </section>
</main>
</body>
</html>
```